Blogging Membership Course Needs a Banner Ad Design

We need a banner ad design for a new membership site called Kitchen Quill Institute which teaches food bloggers how to transform their blog into a full-time dream job through multimedia training modules and a private community.

We would like the design to use colors that are complementary to the attached logo design. The final design should be eye-catching without being obnoxious or "tacky." It should be simple, modern, clean, slightly feminine, and communicate dream-job, transformational business growth and learning (Kitchen Quill *Institute*). Feel free to use the stock images attached or other images with proper disclosure.

See (rough) sales page here: http://kitchenquillinstitute.example/home/

Designs should be 300x250.

Target Market(s)

Advanced food bloggers looking to finally take their blog to full-time status.

Industry/Entity Type

Training

Font styles to use
Sans Serif

Colors
33a6d7
00a890
f68d4d
faa54b
5c5c5c

Requirements
Must have
• Designs should be 300x250.
Should not have
• No spammy or clickbait-looking ads.

```html
<!DOCTYPE html>
<html lang="en">
<head>
<meta charset="utf-8">
<title>Kitchen Quill Institute – Banner Ads</title>
<link href="https://fonts.googleapis.com/css2?family=Oswald:wght@400;500;600&family=Roboto:wght@500&display=swap" rel="stylesheet">
<style>
  :root {
    --stage: #1c1c1e;
    --blue-light: #3fb2e2;
    --blue: #33a6d7;
    --blue-deep: #1e7fb8;
    --orange: #f68d4d;
    --orange-deep: #ef6a2c;
    --yellow: #faa54b;
    --gold: #ffc21a;
    --white: #ffffff;
    --ink: #2a2a2a;
    --grey: #5c5c5c;
  }
  * { box-sizing: border-box; margin: 0; padding: 0; }
  html, body { width: 1200px; height: 680px; overflow: hidden; }
  body { background: var(--stage); position: relative; }

  .banner {
    position: absolute;
    top: 161px;
    width: 453px;
    height: 376px;
    overflow: hidden;
    background: var(--white);
  }
  .banner--desk { left: 113px; }
  .banner--laptop { left: 633px; }

  .banner__photo {
    position: absolute;
    left: 205px; top: 0;
    width: 248px; height: 272px;
  }
  .banner--desk .banner__photo {
    background: linear-gradient(150deg, #f4f4f2 0%, #e4e4e2 45%, #d8d6d4 70%, #ef9fae 100%);
  }
  .banner--laptop .banner__photo {
    background: linear-gradient(135deg, #8a6a4c 0%, #d9d6d0 35%, #c9c6c2 60%, #7d5a3e 100%);
  }

  .banner__rule {
    position: absolute;
    left: 205px; top: 272px;
    width: 248px; height: 5px;
    background: var(--orange-deep);
  }

  .banner__brand {
    position: absolute;
    left: 226px; top: 287px;
    width: 220px;
    text-align: center;
    font-family: "Oswald", sans-serif;
    font-weight: 500;
    color: var(--orange-deep);
    text-transform: uppercase;
    line-height: 1;
    white-space: nowrap;
  }
  .banner__brand-mark {
    display: block;
    width: 12px; height: 12px;
    margin: 0 auto 6px;
    border-radius: 50%;
    background: var(--blue);
  }
  .banner__brand-name { display: block; font-size: 30px; letter-spacing: 0; }
  .banner__brand-sub { display: block; font-size: 14px; letter-spacing: 4px; margin-top: 5px; }

  .banner__panel {
    position: absolute;
    left: 0; top: 0;
    width: 260px; height: 376px;
  }

  .banner__copy {
    position: absolute;
    left: 14px; top: 12px;
    width: 215px;
    font-family: "Oswald", sans-serif;
    color: var(--white);
  }
  .banner__headline {
    font-weight: 400;
    font-size: 36px;
    line-height: 42px;
    letter-spacing: -0.5px;
  }
  .banner__headline-accent {
    display: block;
    color: var(--gold);
    font-weight: 600;
    font-size: 46px;
    line-height: 52px;
    letter-spacing: -1px;
  }
  .banner__divider {
    width: 205px; height: 1px;
    margin: 10px 0 8px;
    background: rgba(255,255,255,0.35);
  }
  .banner__body {
    font-weight: 400;
    font-size: 27px;
    line-height: 31px;
    letter-spacing: -0.5px;
  }

  .banner__cta {
    position: absolute;
    left: 12px; top: 310px;
    width: 182px; height: 46px;
    border-radius: 5px;
    background: linear-gradient(180deg, #ffd24a 0%, var(--gold) 45%, var(--yellow) 100%);
    box-shadow: 0 3px 4px rgba(0,0,0,0.35);
    display: flex; align-items: center; justify-content: center;
    font-family: "Roboto", sans-serif;
    font-weight: 500;
    font-size: 22px;
    color: var(--ink);
    letter-spacing: -0.3px;
  }
</style>
</head>
<body>

  <section class="banner banner--desk" aria-label="Kitchen Quill Institute banner, desk version">
    <div class="banner__photo" role="img" aria-label="Photo from above of hands typing on a laptop on a white desk with pink flowers, sunglasses and a notebook"></div>
    <div class="banner__rule"></div>
    <svg class="banner__panel" viewBox="0 0 260 376" aria-hidden="true">
      <defs>
        <linearGradient id="panelBlueA" x1="0" y1="0" x2="1" y2="1">
          <stop offset="0" stop-color="#3fb2e2"/>
          <stop offset="1" stop-color="#1e7fb8"/>
        </linearGradient>
      </defs>
      <polygon points="0,0 216,0 248,190 216,376 0,376" fill="#ef6a2c"/>
      <polygon points="0,0 206,0 238,190 206,376 0,376" fill="url(#panelBlueA)"/>
    </svg>
    <div class="banner__brand">
      <span class="banner__brand-mark"></span>
      <span class="banner__brand-name">Kitchen Quill</span>
      <span class="banner__brand-sub">Institute</span>
    </div>
    <div class="banner__copy">
      <h2 class="banner__headline">Turn Your<br>Blog Into Your<span class="banner__headline-accent">DREAM JOB</span></h2>
      <div class="banner__divider"></div>
      <p class="banner__body">WITHOUT millions<br>of pageviews or<br>thousands of<br>followers.</p>
    </div>
    <div class="banner__cta">LEARN MORE</div>
  </section>

  <section class="banner banner--laptop" aria-label="Kitchen Quill Institute banner, laptop version">
    <div class="banner__photo" role="img" aria-label="Photo of a person working on a laptop showing a blog page, with a coffee cup on a wooden desk"></div>
    <div class="banner__rule"></div>
    <svg class="banner__panel" viewBox="0 0 260 376" aria-hidden="true">
      <defs>
        <linearGradient id="panelBlueB" x1="0" y1="0" x2="1" y2="1">
          <stop offset="0" stop-color="#3fb2e2"/>
          <stop offset="1" stop-color="#1e7fb8"/>
        </linearGradient>
      </defs>
      <polygon points="0,0 216,0 248,190 216,376 0,376" fill="#ef6a2c"/>
      <polygon points="0,0 206,0 238,190 206,376 0,376" fill="url(#panelBlueB)"/>
    </svg>
    <div class="banner__brand">
      <span class="banner__brand-mark"></span>
      <span class="banner__brand-name">Kitchen Quill</span>
      <span class="banner__brand-sub">Institute</span>
    </div>
    <div class="banner__copy">
      <h2 class="banner__headline">Turn Your<br>Blog Into Your<span class="banner__headline-accent">DREAM JOB</span></h2>
      <div class="banner__divider"></div>
      <p class="banner__body">WITHOUT millions<br>of pageviews or<br>thousands of<br>followers.</p>
    </div>
    <div class="banner__cta">LEARN MORE</div>
  </section>

</body>
</html>
```